The Wagon Rolls Yonder is a food truck, talent show, fundraiser event.

The Belmere Uplift Foundation is hosting a food truck, talent show, fundraiser called The Wagon Rolls Yonder. We need a flyer designed that incorporates a couple of our existing logos. The theme this year is "Summer Kickoff Jam." The event will be held Wednesday, May 23rd from 3-6 pm at the BRAND NEW Northwind Civic Amphitheater (R). I've included some of our logos to incorporate into the flyer. This event is geared towards kids K-12.

Target Market(s)

Kids (K-12) and parents

Industry/Entity Type

Non Profit

Colors

Designer to choose colors to be used in the design.

Requirements
Must have
• Incorporate both logos: Truck (prominent), Foundation logo (not as prominent).
Nice to have
• Might need to have some space to add sponsor logos. Not a must.

```html
<!DOCTYPE html>
<html lang="en">
<head>
<meta charset="utf-8">
<title>Summer Kickoff Jam Flyer</title>
<link rel="stylesheet" href="https://fonts.googleapis.com/css2?family=Open+Sans:wght@300;700;800&family=Lobster&family=Pinyon+Script&family=Dancing+Script:wght@700&display=swap">
<style>
  :root {
    --backdrop: #e6e6e6;
    --flyer-red: #e81c24;
    --burst-tone: #f0585d;
    --bubble-cream: #f4f0e2;
    --ink: #111111;
    --white: #ffffff;
    --foundation-blue: #1f4fa0;
    --truck-blue: #2a8fcf;
    --gold: #e8c21a;
    --megaphone-light: #e4dfd0;
    --megaphone-dark: #2a2a2a;
  }
  * { margin: 0; padding: 0; box-sizing: border-box; }
  html, body {
    width: 1200px; height: 959px; overflow: hidden;
    background: var(--backdrop);
  }
  .flyer {
    position: absolute; left: 290px; top: 40px;
    width: 620px; height: 879px;
    background: var(--flyer-red);
    overflow: hidden;
    box-shadow: 0 6px 18px rgba(0,0,0,0.18);
  }
  .flyer-art { position: absolute; inset: 0; }
  .presenters {
    position: absolute; left: 40px; top: 110px; width: 540px;
    display: flex; align-items: center; justify-content: center; gap: 16px;
    font-family: "Open Sans", sans-serif;
  }
  .foundation-name {
    display: flex; align-items: center; gap: 8px;
    font-weight: 800; font-size: 14px; line-height: 1.15;
    color: var(--foundation-blue); text-transform: uppercase; width: 140px;
  }
  .foundation-name .mark {
    flex: none; width: 14px; height: 14px; border-radius: 50%; background: var(--gold);
  }
  .presents-word {
    font-family: "Pinyon Script", cursive; font-size: 24px; color: #555;
  }
  .truck-name {
    display: flex; align-items: center; gap: 10px;
    font-weight: 800; font-size: 26px; line-height: 1.1;
    color: var(--truck-blue); text-transform: uppercase; width: 250px;
  }
  .truck-name .mark {
    flex: none; width: 34px; height: 34px; border-radius: 50%; background: var(--truck-blue);
  }
  .event-title {
    position: absolute; left: 255px; top: 335px; width: 350px;
    font-family: "Lobster", cursive; font-weight: 400; font-size: 60px; line-height: 1.05;
    color: var(--ink); text-align: center;
    text-shadow: 2px 2px 0 var(--white), -1px -1px 0 var(--white), 1px -1px 0 var(--white), -1px 1px 0 var(--white);
  }
  .event-date {
    position: absolute; left: 255px; top: 480px; width: 350px;
    font-family: "Dancing Script", cursive; font-size: 58px; line-height: 1.1;
    color: var(--white); text-align: center;
  }
  .event-time {
    position: absolute; left: 240px; top: 555px; width: 370px;
    font-family: "Dancing Script", cursive; font-size: 30px; line-height: 1.2;
    color: var(--white); text-align: center;
  }
  .event-at {
    position: absolute; left: 240px; top: 605px; width: 370px;
    font-family: "Open Sans", sans-serif; font-weight: 700; font-size: 26px;
    color: var(--white); text-align: center;
  }
  .venue {
    position: absolute; left: 20px; top: 670px; width: 580px;
    font-family: "Open Sans", sans-serif; color: var(--white); text-align: center;
  }
  .venue-line { display: block; font-weight: 800; font-size: 36px; line-height: 1.2; }
  .venue-line.light { font-weight: 300; font-size: 40px; }
</style>
</head>
<body>
  <main class="flyer">
    <svg class="flyer-art" width="620" height="879" viewBox="0 0 620 879" aria-hidden="true">
      <path class="speech-bubble" d="M0 0 H620 V150 C620 230 520 275 390 282 L330 330 L340 282 C170 282 40 240 0 180 Z" fill="var(--bubble-cream)"/>
    </svg>
    <svg class="burst burst-left" style="position:absolute;left:18px;top:200px" width="80" height="70" viewBox="0 0 80 70" role="img" aria-label="Burst ornament beside the speech bubble">
      <rect width="80" height="70" fill="var(--burst-tone)"/>
    </svg>
    <svg class="burst burst-right" style="position:absolute;left:530px;top:200px" width="70" height="60" viewBox="0 0 70 60" role="img" aria-label="Burst ornament beside the speech bubble">
      <rect width="70" height="60" fill="var(--burst-tone)"/>
    </svg>
    <svg class="megaphone-art" style="position:absolute;left:20px;top:330px" width="230" height="330" viewBox="0 0 230 330" role="img" aria-label="Illustration of a raised fist holding a megaphone">
      <defs>
        <linearGradient id="megaphoneTone" x1="0" y1="0" x2="0" y2="1">
          <stop offset="0" stop-color="var(--megaphone-light)"/>
          <stop offset="1" stop-color="var(--megaphone-dark)"/>
        </linearGradient>
      </defs>
      <rect x="0" y="0" width="230" height="330" rx="20" fill="url(#megaphoneTone)"/>
    </svg>

    <div class="presenters">
      <div class="foundation-name"><span class="mark"></span><span>The Belmere Uplift Foundation</span></div>
      <span class="presents-word">Presents</span>
      <div class="truck-name"><span class="mark"></span><span>The Wagon Rolls Yonder</span></div>
    </div>

    <h1 class="event-title">Summer Kickoff Jam</h1>
    <p class="event-date">May 23</p>
    <p class="event-time">Wednesday, From 3-6 pm</p>
    <p class="event-at">@</p>
    <p class="venue">
      <span class="venue-line">BRAND NEW Northwind Civic</span>
      <span class="venue-line light">Amphitheater (R)</span>
    </p>
  </main>
</body>
</html>
```